"Made in Chicago" Baby Shower Invitation

I need a design for a baby shower invitation with the headline and theme of "Made in Chicago". The design should incorporate the colors/design of the Chicago flag. I have attached an image of the flag for your reference. The design should be sized 5-1/2 wide x 8-1/2 long. I want to be able to print two to a page on a standard 8-1/2 X 11" piece of (nice quality) paper on a standard home printer.
Copy:
Made in Chicago Baby Shower
For: Marla & Gordon
Date: Saturday, April 5, 2014
Time: 7:00 p.m.
Place: 27 West Halbrook Ave, 4B
RSVP by April 1 to Nadia Verholm/312-555-0193

Hello Designers - I corrected the size requirements of the invitation (bad math before) and added a few more notes of preference. Looking for a design that is more clean and graphic and less traditional, soft baby shower look. Thank you!

Friends & family of the 20-sometthing, urban professional couple who are having a baby.

Baby

Must have
• Chicago flag colors and/or image, the words "made in Chicago", and the (revised) size indicated.
Should not have
• Anything inappropriate or offensive to grandmother of said couple.

```html
<!DOCTYPE html>
<html lang="en">
<head>
<meta charset="utf-8">
<title>Made in Chicago Baby Shower Invitation</title>
<link rel="stylesheet" href="https://fonts.googleapis.com/css2?family=Cinzel:wght@400;500&family=Dancing+Script:wght@500;600&family=Sniglet:wght@800&display=swap">
<style>
  :root {
    --sky: #cdeefb;
    --sky-deep: #bfe6f8;
    --flag-red: #e8141c;
    --label-blue: #6a9bb3;
    --outline-blue: #9fd4ef;
    --snow: #ffffff;
    --rsvp-blue: #a9d9f0;
  }
  html, body {
    margin: 0;
    padding: 0;
    width: 1200px;
    height: 2400px;
    overflow: hidden;
  }
  .invitation {
    position: relative;
    width: 1200px;
    height: 2400px;
    background: var(--sky);
    overflow: hidden;
  }
  .starfield {
    position: absolute;
    inset: 0;
    background: radial-gradient(ellipse at 50% 55%, var(--sky) 0%, var(--sky) 55%, var(--sky-deep) 100%);
  }
  .headline {
    position: absolute;
    left: 0;
    width: 1200px;
    text-align: center;
    color: var(--flag-red);
    margin: 0;
    line-height: 1;
  }
  .headline-made { top: 105px; font: 400 140px/1 "Cinzel", serif; font-variant: small-caps; }
  .headline-in   { top: 290px; font: 400 140px/1 "Cinzel", serif; font-variant: small-caps; }
  .headline-city { top: 450px; font: 600 225px/1 "Dancing Script", cursive; }
  .event-title {
    position: absolute;
    left: 0;
    width: 1200px;
    text-align: center;
    color: var(--snow);
    font: 800 200px/1 "Sniglet", sans-serif;
    -webkit-text-stroke: 10px var(--outline-blue);
    paint-order: stroke fill;
    margin: 0;
  }
  .event-title-baby { top: 740px; }
  .event-title-shower { top: 940px; font-size: 220px; }
  .details {
    position: absolute;
    left: 133px;
    width: 920px;
    top: 1310px;
    margin: 0;
  }
  .detail-row {
    display: flex;
    justify-content: space-between;
    align-items: baseline;
    height: 117px;
  }
  .detail-label {
    font: 400 38px/1 "Cinzel", serif;
    color: var(--label-blue);
    font-variant: small-caps;
    text-transform: lowercase;
  }
  .detail-value {
    font: 400 48px/1 "Cinzel", serif;
    color: var(--flag-red);
    font-variant: small-caps;
    margin: 0;
  }
  .rsvp {
    position: absolute;
    left: 0;
    width: 1200px;
    top: 1850px;
    text-align: center;
    color: var(--rsvp-blue);
    font: 500 92px/1.55 "Dancing Script", cursive;
    text-shadow: 0 0 6px var(--snow), 0 0 3px var(--snow);
    margin: 0;
  }
</style>
</head>
<body>
<main class="invitation">
  <div class="starfield" role="img" aria-label="Pale sky-blue background scattered with small red outlined stars and soft white six-pointed stars"></div>

  <h1>
    <span class="headline headline-made">Made</span>
    <span class="headline headline-in">In</span>
    <span class="headline headline-city">Chicago</span>
  </h1>

  <h2>
    <span class="event-title event-title-baby">Baby</span>
    <span class="event-title event-title-shower">Shower</span>
  </h2>

  <dl class="details">
    <div class="detail-row"><dt class="detail-label">For:</dt><dd class="detail-value">Marla &amp; Gordon</dd></div>
    <div class="detail-row"><dt class="detail-label">Date:</dt><dd class="detail-value">Saturday, April 5, 2014</dd></div>
    <div class="detail-row"><dt class="detail-label">Time:</dt><dd class="detail-value">7.00 pm</dd></div>
    <div class="detail-row"><dt class="detail-label">Place:</dt><dd class="detail-value">27 West Halbrook Ave, 4B</dd></div>
  </dl>

  <p class="rsvp">RSVP by April 1 to<br>Nadia Verholm/312-555-0193</p>
</main>
</body>
</html>
```